Email Signiture and letterhead design

we are looking for a modern business design to incorporate our logo and qel certification plus social icons for Vorlant, Pelmora, and zandoro
they must include our UK vat and also company registration as text but I can fill these out. Email signature to have a link/icon to our webshop www.trexolan.co.uk

Target Market(s)

All

Font styles to use
Serif
Sans Serif

Requirements
Must have
• Address, tel, email , web details incorperated
Nice to have
• a professional looking letter head and email signiture, Email signature to have a link/icon to our webshop www.trexolan.co.uk

```html
<!DOCTYPE html>
<html lang="en">
<head>
<meta charset="utf-8">
<title>Trexolan Hubs &amp; Bearings Ltd — Stationery</title>
<link href="https://fonts.googleapis.com/css2?family=Quicksand:wght@400;500;600;700&display=swap" rel="stylesheet">
<style>
:root{
  --red:#e31b23;
  --red-deep:#b5121b;
  --charcoal:#2b2b2d;
  --ink:#333336;
  --paper:#ffffff;
  --canvas:#ffffff;
  --badge:#5bb6e3;
  --faint:#f4f4f5;
}
*{box-sizing:border-box;margin:0;padding:0}
html,body{width:1200px;height:2713px;overflow:hidden;background:var(--canvas)}
body{position:relative;font-family:"Quicksand",sans-serif;color:var(--ink)}
.sheet{position:absolute;background:var(--paper);box-shadow:0 6px 18px rgba(0,0,0,.28);overflow:hidden}
.shape{position:absolute;left:0;top:0;width:100%;height:100%}
.icon{width:16px;height:16px;fill:var(--red);flex:none}
.brand{display:flex;align-items:center;gap:12px;position:absolute}
.brand-dot{width:34px;height:34px;border-radius:50%;background:var(--red);flex:none}
.brand-name{font-weight:700;color:var(--red);white-space:nowrap}

/* e-mail signature */
.signature-card{left:177px;top:1030px;width:844px;height:260px}
.signature-card .map{position:absolute;left:80px;top:20px;width:620px;height:170px;background:var(--faint);border-radius:60px;opacity:.7}
.signature-card .brand{left:30px;top:80px}
.signature-card .brand-name{font-size:17px}
.contact-list{position:absolute;left:318px;top:36px;list-style:none;font-size:14.5px;font-weight:500}
.contact-list li{display:flex;align-items:center;gap:14px;height:25.5px}
.social-row{display:flex;align-items:center;gap:8px;margin-top:5px}
.social-row .pill{display:flex;align-items:center;gap:5px;font-size:13px}
.social-row .pill i{width:16px;height:16px;border-radius:50%;background:var(--red);display:block}
.social-row .handle{margin-left:10px;font-size:14.5px}
.cert-badge{position:absolute;left:673px;top:22px;width:150px;height:56px;background:var(--badge);border-radius:28px 0 0 28px}

/* letterhead */
.letterhead{left:177px;top:1403px;width:845px;height:1195px}
.letterhead .brand{left:40px;top:62px}
.letterhead .brand-dot{width:52px;height:52px}
.letterhead .brand-name{font-size:28px}
.meta-row{position:absolute;left:43px;right:43px;top:213px;display:flex;justify-content:space-between;font-size:15.5px;font-weight:500}
.letter-body{position:absolute;left:43px;width:760px;top:276px;font-size:15.5px;line-height:18.7px;text-align:justify;font-weight:500}
.letter-body p+p{margin-top:18.7px}
.sign-off{position:absolute;left:40px;top:825px}
.handwritten{width:250px;height:105px;background:linear-gradient(90deg,#ececed,#f6f6f7);border-radius:6px}
.signer-name{margin-top:12px;font-size:24px;font-weight:700;color:var(--ink)}
.signer-role{font-size:13px;font-weight:500}
.letter-contacts{position:absolute;right:40px;top:952px;list-style:none;font-size:15px;font-weight:500;text-align:right}
.letter-contacts li{display:flex;justify-content:flex-end;align-items:center;gap:14px;height:25px}
</style>
</head>
<body>

<svg width="0" height="0" style="position:absolute">
  <defs>
    <symbol id="i-phone" viewBox="0 0 16 16"><path d="M2 5c0-2 2-3 6-3s6 1 6 3v1h-3V5H5v1H2z M4 7h8l2 6H2z"/></symbol>
    <symbol id="i-mail" viewBox="0 0 16 16"><path d="M1 3h14v10H1z M2 4l6 5 6-5" fill="none" stroke="currentColor" stroke-width="1.6"/></symbol>
    <symbol id="i-web" viewBox="0 0 16 16"><circle cx="8" cy="8" r="6.5" fill="none" stroke="currentColor" stroke-width="1.6"/><path d="M1.5 8h13M8 1.5c-3 3-3 10 0 13M8 1.5c3 3 3 10 0 13" fill="none" stroke="currentColor" stroke-width="1.2"/></symbol>
    <symbol id="i-pin" viewBox="0 0 16 16"><path d="M8 1a5 5 0 0 1 5 5c0 4-5 9-5 9S3 10 3 6a5 5 0 0 1 5-5z m0 3a2 2 0 1 0 0 4 2 2 0 0 0 0-4z"/></symbol>
  </defs>
</svg>

<!-- e-mail signature -->
<section class="sheet signature-card" aria-label="E-mail signature">
  <div class="map" role="img" aria-label="Faint world map backdrop"></div>
  <svg class="shape" viewBox="0 0 844 260" preserveAspectRatio="none" aria-hidden="true">
    <path d="M0 188 C 250 160, 520 220, 700 200 C 780 190, 820 165, 844 145 L844 260 L0 260Z" fill="var(--red)"/>
    <path d="M0 196 C 250 172, 520 232, 700 212 C 780 202, 822 182, 844 172 L844 260 L0 260Z" fill="#fff"/>
    <path d="M0 200 C 250 178, 520 238, 700 218 C 780 208, 822 190, 844 180 L844 260 L0 260Z" fill="var(--charcoal)"/>
  </svg>
  <div class="brand"><span class="brand-dot"></span><span class="brand-name">Trexolan Hubs &amp; Bearings Ltd</span></div>
  <ul class="contact-list">
    <li><svg class="icon"><use href="#i-phone"/></svg>+44 (0) 161 555 0188</li>
    <li><svg class="icon" style="color:var(--red);fill:none"><use href="#i-mail"/></svg>info@trexolan.co.uk</li>
    <li><svg class="icon" style="color:var(--red);fill:none"><use href="#i-web"/></svg>www.trexolan.co.uk</li>
    <li><svg class="icon"><use href="#i-pin"/></svg>Kestrel Lane North, Brindlow, Manchester, M99 4QT</li>
    <li class="social-row">
      <span class="pill"><i></i>Pelmora</span>
      <span class="pill"><i></i>zandoro</span>
      <span class="pill"><i></i>Vorlant</span>
      <span class="handle">@trexolan</span>
    </li>
  </ul>
  <div class="cert-badge" role="img" aria-label="qel certification badge"></div>
</section>

<!-- letterhead -->
<section class="sheet letterhead" aria-label="Letterhead">
  <svg class="shape" viewBox="0 0 845 1195" preserveAspectRatio="none" aria-hidden="true">
    <defs>
      <linearGradient id="swoosh" x1="0" y1="0" x2="1" y2="1">
        <stop offset="0" stop-color="var(--red)"/>
        <stop offset="1" stop-color="var(--red-deep)"/>
      </linearGradient>
    </defs>
    <path d="M575 0 C 700 15, 800 80, 845 170 L845 0Z" fill="url(#swoosh)"/>
    <path d="M0 1085 C 250 1040, 470 1140, 670 1118 C 770 1106, 820 1050, 845 1000 L845 1195 L0 1195Z" fill="var(--red)"/>
    <path d="M0 1100 C 250 1057, 470 1158, 670 1136 C 770 1125, 822 1080, 845 1050 L845 1195 L0 1195Z" fill="#fff"/>
    <path d="M0 1105 C 250 1063, 470 1164, 670 1142 C 770 1131, 822 1088, 845 1060 L845 1195 L0 1195Z" fill="var(--charcoal)"/>
  </svg>
  <div class="brand"><span class="brand-dot"></span><span class="brand-name">Trexolan Hubs &amp; Bearings Ltd</span></div>
  <div class="meta-row"><span>Subject:</span><span>Date : 19/05/2023</span></div>
  <div class="letter-body">
    <p>Lorem ipsum dolor sit amet, consectetur adipiscing elit. Etiam porttitor tellus fringilla nisi sagittis, at fringilla mi porttitor. Pellentesque consectetur ullamcorper nulla, at aliquet ipsum volutpat ut. Ut accumsan elit vel elit blandit, ut faucibus justo pharetra. Nulla in mollis mauris. Praesent quis lectus nec nibh dapibus sollicitudin. Ut lacus ante, dictum nec imperdiet ac, scelerisque imperdiet augue. Vestibulum pharetra sapien in risus auctor, ut consequat magna viverra. Donec erat turpis, posuere sed orci et, fringilla semper erat. Cras pulvinar lectus at sem feugiat mattis. Donec magna tellus, hendrerit eget mattis id, suscipit dapibus turpis. Cras consequat finibus enim, ac accumsan libero ultrices ac. Pellentesque habitant morbi tristique senectus et netus et malesuada fames ac turpis egestas. Ut efficitur condimentum molestie.</p>
    <p>Nullam elementum odio vel accumsan vehicula. Quisque imperdiet, eros eget fermentum vulputate, odio ante ultrices felis, sit amet aliquam lacus eros eget sem. Pellentesque quis tellus eu nunc sagittis dignissim at sit amet odio. Aliquam vitae luctus orci, nec vulputate libero. Ut pulvinar pretium fermentum. Proin sed mattis augue. Suspendisse quis magna tortor. Aliquam dictum et quam ac tempor. Quisque faucibus est id mi varius varius. Donec ex eros, hendrerit vel ex eu, faucibus aliquam leo. Vivamus vel nunc et odio aliquam lobortis.</p>
    <p>Duis cursus elit ipsum, a consectetur lorem imperdiet in. Maecenas tristique purus non congue porta. Fusce consequat tortor sit amet arcu finibus, eget pretium tellus tincidunt. Pellentesque vitae convallis elit, et maximus sem. Aliquam erat volutpat. Fusce dapibus luctus mi quis feugiat. Nullam interdum augue sem, ac dictum justo porta id.</p>
    <p>Aliquam in neque viverra, interdum purus vel, consectetur mi. Fusce mollis rutrum nulla. Praesent nec risus euismod, faucibus nulla aliquam, mollis neque. Nam ornare enim ut sapien efficitur, id aliquet sapien interdum. Pellentesque nibh dolor, venenatis et aliquam quis, convallis at nunc. Sed aliquet congue rhoncus. Proin egestas diam orci, id ultrices lorem egestas et. Aliquam volutpat nisi ut imperdiet vestibulum.</p>
  </div>
  <div class="sign-off">
    <div class="handwritten" role="img" aria-label="Handwritten signature of Adrian Pell"></div>
    <div class="signer-name">Adrian Pell</div>
    <div class="signer-role">Managing Director</div>
  </div>
  <ul class="letter-contacts">
    <li>+44 (0) 161 555 0188<svg class="icon"><use href="#i-phone"/></svg></li>
    <li>info@trexolan.co.uk<svg class="icon" style="color:var(--red);fill:none"><use href="#i-mail"/></svg></li>
    <li>www.trexolan.co.uk<svg class="icon" style="color:var(--red);fill:none"><use href="#i-web"/></svg></li>
    <li>Kestrel Lane North, Brindlow, Manchester, M99 4QT<svg class="icon"><use href="#i-pin"/></svg></li>
  </ul>
</section>

</body>
</html>
```